design a web site for equipment and software pos company

We would a web site similar to the site we whited labed our rtil system .https://tryplimvo.com/
website would be on RkTillDepot.com
we would a contact page
877-555-0142

We do not want an exact copy just something similar .
we are tablet po system

we are at

we are selling hardware and software

rk till depot
41 fernhollow ln
warren, nj 07318
we are cloud based system

Target Market(s)

any retail merchant

Industry/Entity Type

credit card processing in POS asystems

Coding

Coded - Design and coding required

Number of Pages Required

5+ page

Requirements
Must have
• be able to connect hostwren hosting
Nice to have
• modern looking site
Should not have
• any red

```html
<!DOCTYPE html>
<html lang="en">
<head>
<meta charset="utf-8">
<title>RK Till Depot</title>
<link href="https://fonts.googleapis.com/css2?family=Lato:wght@400;700&family=Work+Sans:wght@500;600&display=swap" rel="stylesheet">
<style>
:root{
  --white:#ffffff;
  --ink:#111111;
  --text:#222222;
  --yellow:#f2c417;
  --yellow-soft:#fde9a6;
  --lavender:#dfe1fb;
  --footer:#121212;
  --muted:#8a8a8a;
  --salmon:#f08a7a;
  --olive:#b89a00;
  --cyan:#38b6c8;
}
*{box-sizing:border-box;margin:0;padding:0}
html,body{width:1200px;height:900px;overflow:hidden;background:var(--white)}
body{position:relative;font-family:"Lato",sans-serif;color:var(--text)}
.page{position:absolute;left:491.5px;top:26px;width:400px;height:1562px;transform:scale(0.5425);transform-origin:0 0;background:var(--white);outline:1px solid #bbb;overflow:hidden}
.abs{position:absolute}
.heading{font-family:"Work Sans",sans-serif;font-weight:600;color:var(--ink);letter-spacing:.03em}
.body-copy{font-size:6px;line-height:11px;color:var(--text)}

/* hero */
.hero{left:0;top:0;width:400px;height:257px;background:linear-gradient(180deg,#a9a9a9 0%,#bdbdbd 45%,#d6d6d6 80%,#e9e9e9 100%)}
.brand{left:22px;top:9px;font-family:"Lato",sans-serif;font-weight:700;font-size:8px;color:var(--white);display:flex;align-items:center;gap:3px}
.brand .mark{width:7px;height:7px;background:var(--yellow)}
.nav{top:13px;font-size:5px;color:var(--white)}
.nav-cta{left:337px;top:9px;width:38px;height:15px;background:var(--yellow);color:var(--white);font-size:5px;display:flex;align-items:center;justify-content:center}
.hero-title{left:0;top:52px;width:400px;text-align:center;font-family:"Work Sans",sans-serif;font-weight:500;font-size:20px;line-height:25px;color:var(--white);letter-spacing:.04em}
.hero-title .accent{color:var(--yellow)}

/* about */
.about-title{left:23px;top:312px;font-size:11px;line-height:14px}
.about-rule{left:23px;top:341px;width:40px;height:1.5px;background:var(--yellow)}
.about-copy{left:23px;top:350px;width:178px}
.photo{background:linear-gradient(135deg,#2c2f45,#5a5f7a 50%,#8d7b6d)}

/* easy */
.easy-title{left:60px;top:462px;width:280px;text-align:center;font-size:14px;line-height:17px}
.easy-copy{left:80px;top:498px;width:240px;text-align:center;font-size:5.5px;line-height:10px}
.easy-link{left:0;top:525px;width:400px;text-align:center;font-size:5px;color:var(--yellow)}
.payment-photo{left:0;top:528px;width:400px;height:224px;background:linear-gradient(120deg,#f4f4f4,#e6e6e6 55%,#d7e9e2 75%,#eeeeee)}

/* inventory */
.inventory{left:0;top:752px;width:400px;height:203px;background:var(--lavender)}
.inv-title{left:23px;top:810px;width:190px;font-size:11px;line-height:14px}
.inv-copy{left:23px;top:842px;width:125px}
.btn-outline{left:23px;top:884px;width:54px;height:13px;border:1px solid var(--ink);font-size:5px;display:flex;align-items:center;justify-content:center;color:var(--ink)}
.store-photo{background:linear-gradient(135deg,#6b5a48,#b9a58b 45%,#8a4a3a 70%,#d8d3cc)}

/* offer */
.offer-title{left:0;top:985px;width:400px;text-align:center;font-size:17px}
.offer{top:1020px;width:100px}
.offer .dot{position:absolute;left:-9px;top:0;width:18px;height:18px;border-radius:50%}
.offer h3{position:relative;font-size:6.5px;line-height:11px;font-weight:700;color:var(--ink);margin-top:4px}
.offer p{position:relative;margin-top:5px;font-size:6px;line-height:9.6px}

/* cta */
.cta{left:0;top:1118px;width:400px;height:251px;background:var(--yellow-soft)}
.devices{left:0;top:1152px;width:142px;height:185px;background:linear-gradient(135deg,#2a2a2a,#e9efe9 15%,#ffffff 50%,#dfe8df 85%,#1d1d1d)}
.cta-title{left:179px;top:1186px;width:190px;font-size:13px;line-height:19px}
.cta-copy{left:179px;top:1226px;width:180px;font-size:5.5px;line-height:11px}
.cta-sub{left:179px;top:1258px;font-family:"Work Sans",sans-serif;font-weight:500;font-size:9px;color:var(--ink)}
.cta-sub-copy{left:179px;top:1272px;font-size:5.5px}
.btn-solid{left:179px;top:1290px;width:65px;height:13px;background:var(--yellow);font-size:5px;display:flex;align-items:center;justify-content:center;color:var(--ink);font-weight:700}

/* footer */
.footer{left:0;top:1369px;width:400px;height:193px;background:var(--footer)}
.footer-brand{left:36px;top:1410px;font-weight:700;font-size:11px;color:var(--white);display:flex;align-items:center;gap:4px}
.footer-brand .mark{width:9px;height:9px;background:var(--yellow)}
.footer-about{left:36px;top:1440px;width:90px;font-size:4.5px;line-height:8.5px;color:#cfcfcf}
.footer-col{top:1440px;font-size:5px;line-height:11px;color:#d8d8d8}
.footer-col .label{color:var(--muted);letter-spacing:.04em}
.newsletter{left:292px;top:1442px;width:70px;height:10px;display:flex}
.newsletter .field{flex:1;background:#6b6b6b;font-size:3.5px;color:#ddd;display:flex;align-items:center;padding-left:3px}
.newsletter .join{width:22px;background:#000;font-size:3.5px;color:#ddd;display:flex;align-items:center;justify-content:center}
.social{top:1461px;width:5px;height:5px;border-radius:50%;background:#d8d8d8}
</style>
</head>
<body>
<main class="page">

  <section class="hero abs" role="img" aria-label="Photo of hands typing on a laptop on a white desk beside a potted plant"></section>
  <div class="brand abs"><span class="mark"></span>RK Till Depot</div>
  <nav>
    <span class="nav abs" style="left:97px">Features</span>
    <span class="nav abs" style="left:141px">Business Types</span>
    <span class="nav abs" style="left:201px">Products</span>
    <span class="nav abs" style="left:246px">Partners</span>
    <span class="nav abs" style="left:290px">About Us</span>
    <span class="nav-cta abs">Contact</span>
  </nav>
  <h1 class="hero-title abs">Grow Your Business With<br><span class="accent">RK</span> Till Depot</h1>

  <h2 class="about-title heading abs">ABOUT<br>RK TILL DEPOT</h2>
  <div class="about-rule abs"></div>
  <p class="about-copy body-copy abs">Lorem ipsum dolor sit amet, consectetur adipiscing elit. Risus suspendisse elit pretium nulla. Risus arcu vitae tincidunt neque neque nunc adipiscing. Proin non cras interdum placerat dictum amet vel. Vitae dolor, sed tellus egestas.</p>
  <div class="photo abs" style="left:225px;top:301px;width:150px;height:114px" role="img" aria-label="Photo of a team meeting around a laptop"></div>

  <h2 class="easy-title heading abs">One of the world’s easiest POS system to use</h2>
  <p class="easy-copy abs">Lorem ipsum dolor sit amet, consectetur adipiscing elit. Risus suspendisse elit pretium nulla. Risus arcu vitae tincidunt neque neque nunc adipiscing.</p>
  <a class="easy-link abs">Learn more about RK Till Depot →</a>
  <div class="payment-photo abs" role="img" aria-label="Photo of a card terminal printing a receipt while a phone pays contactless"></div>

  <section class="inventory abs"></section>
  <h2 class="inv-title heading abs">Powerful inventory management to help maximize your profits</h2>
  <p class="inv-copy body-copy abs">Effortlessly sell, manage, report and grow your retail business in every way with RK Till Depot.</p>
  <a class="btn-outline abs">Our services</a>
  <div class="store-photo abs" style="left:225px;top:797px;width:150px;height:113px" role="img" aria-label="Photo of a shop worker at a tablet checkout counter"></div>

  <h2 class="offer-title heading abs">What we offer</h2>
  <div class="offer abs" style="left:40px"><span class="dot" style="background:var(--salmon)"></span><h3>Fully automated and synchronized functionality</h3><p>Lorem ipsum dolor sit amet, consectetur adipiscing elit. Risus suspendisse elit pretium nulla. Risus arcu vitae tincidunt</p></div>
  <div class="offer abs" style="left:158px"><span class="dot" style="background:var(--olive)"></span><h3>Deeper business insights reporting</h3><p>Lorem ipsum dolor sit amet, consectetur adipiscing elit. Risus suspendisse elit pretium nulla. Risus arcu vitae tincidunt</p></div>
  <div class="offer abs" style="left:277px"><span class="dot" style="background:var(--cyan)"></span><h3>Openess for itegration</h3><p style="margin-top:16px">Lorem ipsum dolor sit amet, consectetur adipiscing elit. Risus suspendisse elit pretium nulla. Risus arcu vitae tincidunt</p></div>

  <section class="cta abs"></section>
  <div class="devices abs" role="img" aria-label="Tablet and phone showing sales dashboard charts"></div>
  <h2 class="cta-title heading abs">Unlock your retail super power with RK Till</h2>
  <p class="cta-copy abs">Contact or chat with our team to find out how RK Till is right for you and your business</p>
  <h3 class="cta-sub abs">Try RK Till now</h3>
  <p class="cta-sub-copy abs">Discover how easy it is to transform your retail.</p>
  <a class="btn-solid abs">Contact us now</a>

  <footer class="footer abs"></footer>
  <div class="footer-brand abs"><span class="mark"></span>RK Till Depot</div>
  <p class="footer-about abs">We are here for you and your future. Trust us and start growing your business with RK Till Depot</p>
  <div class="footer-col abs" style="left:152px"><div class="label">COMPANY</div><div>About Us</div><div>Features</div><div>Business types</div><div>Products</div></div>
  <div class="footer-col abs" style="left:217px"><div class="label">HELP &amp; SUPPORT</div><div>Contact Us</div><div>Help center</div><div>FAQs</div></div>
  <div class="newsletter abs"><span class="field">Enter email here</span><span class="join">Join Us</span></div>
  <span class="social abs" style="left:320px"></span>
  <span class="social abs" style="left:338px"></span>
  <span class="social abs" style="left:356px"></span>

</main>
</body>
</html>
```